Charity fundraising company - need eDM design!

We are a telemarketing company working with charities to raise money from individuals via regular monthly direct debits or credit card payments. The audience for this eDM is a few hundred fundraising managers. We want to provide a clearly laid-out email to deliver our offer of a free telemarketing consultation.

The eDM will be sent via Mailchimp.

Industry/Entity Type

Charity

Logo Text

KELP Dial

Font styles to use
Sans Serif
Other font styles liked:
• Helvetica Neue

Requirements
Nice to have
• Our values:
• Storytelling with passion
• Fundraising with integrity
• Results that deliver a strong return on your charity's investment.
Should not have
• Logo at the top of the eDM (please place at the bottom)

```html
<!DOCTYPE html>
<html lang="en">
<head>
<meta charset="utf-8">
<title>KELP Dial – Regular Givers eDM</title>
<link rel="stylesheet" href="https://fonts.googleapis.com/css2?family=Open+Sans:wght@400;600;700&display=swap">
<style>
  :root {
    --backdrop: #47474a;
    --paper: #ffffff;
    --top-strip: #f8f8f8;
    --navy: #3f3d4f;
    --green: #8cc043;
    --text-grey: #6f6f6f;
    --heading-grey: #707070;
    --footer-grey: #ececec;
    --accent-blue: #3aa8db;
    --white: #ffffff;
  }
  * { box-sizing: border-box; margin: 0; padding: 0; }
  html, body { width: 960px; height: 1200px; overflow: hidden; }
  body {
    background: var(--backdrop);
    font-family: "Open Sans", "Helvetica Neue", Arial, sans-serif;
    position: relative;
  }
  .email {
    position: absolute;
    left: 120px;
    top: 208px;
    width: 720px;
    background: var(--paper);
  }
  .top-strip { height: 44px; background: var(--top-strip); }
  .headline-band {
    height: 56px;
    background: var(--navy);
    color: var(--white);
    font-size: 24px;
    font-weight: 600;
    display: flex; align-items: center; justify-content: center;
  }
  .hero { display: flex; height: 221px; }
  .hero-pitch {
    width: 50%;
    background: var(--green);
    color: var(--white);
    font-size: 20px;
    font-weight: 700;
    line-height: 1.3;
    text-align: center;
    display: flex; align-items: center; justify-content: center;
    padding: 0 40px;
  }
  .hero-photo {
    width: 50%;
    background: linear-gradient(135deg, #2b2b2e 0%, #4a3f38 45%, #1a1a1c 100%);
  }
  .offer { padding: 14px 0 0; }
  .offer-title {
    text-align: center;
    font-size: 21px;
    color: var(--heading-grey);
    font-weight: 400;
    margin-bottom: 20px;
  }
  .promise-list { list-style: none; padding: 0 28px 0 20px; }
  .promise-list li {
    display: flex; align-items: flex-start;
    font-size: 15.5px;
    line-height: 1.35;
    color: var(--text-grey);
    margin-bottom: 13px;
  }
  .promise-list svg { flex: 0 0 22px; margin: 0 15px 0 0; }
  .cta {
    display: block;
    width: 382px; height: 91px;
    margin: 16px auto 0;
    border-radius: 46px;
    background: var(--green);
    color: var(--white);
    text-align: center;
    text-decoration: none;
    padding-top: 22px;
  }
  .cta-main { display: block; font-size: 17px; font-weight: 700; letter-spacing: 0.2px; }
  .cta-sub { display: block; font-size: 15.5px; font-weight: 700; margin-top: 6px; }
  .contact-bar {
    margin-top: 41px;
    height: 85px;
    background: var(--footer-grey);
    display: flex; align-items: center;
    padding: 0 14px;
  }
  .brand {
    display: flex; align-items: center; gap: 10px;
    width: 206px;
    color: #a3232b;
    font-size: 22px; font-weight: 700;
  }
  .brand-dot { width: 18px; height: 18px; border-radius: 50%; background: #a3232b; }
  .address {
    display: flex; align-items: flex-start; gap: 8px;
    width: 290px;
    font-size: 11.5px; font-weight: 600; line-height: 1.45;
    color: var(--text-grey);
  }
  .contact-lines { display: flex; flex-direction: column; gap: 8px; }
  .contact-line {
    display: flex; align-items: center; gap: 18px;
    font-size: 11.5px; font-weight: 600; color: var(--text-grey);
  }
  .legal-bar {
    height: 41px;
    background: var(--navy);
    color: var(--white);
    font-size: 15.5px;
    display: flex; align-items: center; justify-content: space-between;
    padding: 0 38px 0 35px;
  }
  .legal-bar a { color: var(--white); text-decoration: none; }
</style>
</head>
<body>
  <main class="email">
    <div class="top-strip"></div>
    <header class="headline-band">Want more regular givers for your cause?</header>

    <section class="hero">
      <p class="hero-pitch">KELP Dial is Australia’s leading telemarketing specialist for acquiring new regular givers through lead generation.</p>
      <div class="hero-photo" role="img" aria-label="Smiling call centre agent wearing a headset at his desk"></div>
    </section>

    <section class="offer">
      <h2 class="offer-title">Speak to us today and we will:</h2>
      <ul class="promise-list">
        <li>
          <svg width="22" height="22" viewBox="0 0 22 22" aria-hidden="true"><path d="M18 9.5A8 8 0 1 1 14.5 4" fill="none" stroke="#7a7a7a" stroke-width="2.6" stroke-linecap="round"/><path d="M6.5 10.5l4 4L20 4" fill="none" stroke="#7a7a7a" stroke-width="2.8" stroke-linecap="round" stroke-linejoin="round"/></svg>
          Run a no-obligation TM donor acquisition feasibility assessment for you.
        </li>
        <li>
          <svg width="22" height="22" viewBox="0 0 22 22" aria-hidden="true"><path d="M18 9.5A8 8 0 1 1 14.5 4" fill="none" stroke="#7a7a7a" stroke-width="2.6" stroke-linecap="round"/><path d="M6.5 10.5l4 4L20 4" fill="none" stroke="#7a7a7a" stroke-width="2.8" stroke-linecap="round" stroke-linejoin="round"/></svg>
          Offer a Cost Per Acquisition model, with a sliding scale of fees based on the volume of leads provided.
        </li>
        <li>
          <svg width="22" height="22" viewBox="0 0 22 22" aria-hidden="true"><path d="M18 9.5A8 8 0 1 1 14.5 4" fill="none" stroke="#7a7a7a" stroke-width="2.6" stroke-linecap="round"/><path d="M6.5 10.5l4 4L20 4" fill="none" stroke="#7a7a7a" stroke-width="2.8" stroke-linecap="round" stroke-linejoin="round"/></svg>
          Handle the entire data ordering and management process for you at no additional cost.
        </li>
      </ul>
      <a class="cta" href="#">
        <span class="cta-main">FREE NO-OBLIGATION CONSULTATION</span>
        <span class="cta-sub">Drop us a line today...</span>
      </a>
    </section>

    <footer>
      <div class="contact-bar">
        <div class="brand"><span class="brand-dot"></span>KELP Dial</div>
        <div class="address">
          <svg width="18" height="18" viewBox="0 0 18 18" aria-hidden="true"><circle cx="9" cy="9" r="7.5" fill="none" stroke="var(--accent-blue)" stroke-width="1.4"/><path d="M9 13.5s-3-3-3-5.2a3 3 0 0 1 6 0c0 2.2-3 5.2-3 5.2z" fill="none" stroke="var(--accent-blue)" stroke-width="1.3"/></svg>
          <span>Suite 3.01, Level 3, 18 Harbour Lane,<br>Sydney, NSW, 2000</span>
        </div>
        <div class="contact-lines">
          <div class="contact-line">
            <svg width="18" height="18" viewBox="0 0 18 18" aria-hidden="true"><circle cx="9" cy="9" r="7.5" fill="none" stroke="var(--accent-blue)" stroke-width="1.4"/><path d="M6.3 5.5l1.4-.3.8 2-1 .8a5 5 0 0 0 2.5 2.5l.8-1 2 .8-.3 1.4c-3.5.3-6.5-2.7-6.2-6.2z" fill="var(--accent-blue)"/></svg>
            02 5550 1234
          </div>
          <div class="contact-line">
            <svg width="18" height="18" viewBox="0 0 18 18" aria-hidden="true"><circle cx="9" cy="9" r="7.5" fill="none" stroke="var(--accent-blue)" stroke-width="1.4"/><path d="M7.8 10.2l2.4-2.4M8.8 6.6l.9-.9a1.6 1.6 0 0 1 2.3 2.3l-.9.9M9.2 11.4l-.9.9A1.6 1.6 0 0 1 6 10l.9-.9" fill="none" stroke="var(--accent-blue)" stroke-width="1.3" stroke-linecap="round"/></svg>
            www.kelpdial.com
          </div>
        </div>
      </div>
      <div class="legal-bar">
        <span>KELP Dial 2016 All rights reserved.</span>
        <a href="#">Unsubscribe here</a>
      </div>
    </footer>
  </main>
</body>
</html>
```